依頼詳細
作りたいチラシのイメージは、「参考画像.jpg」の通りです。

裏面のデザイン(価格表)は完成しておりますので、デザインの雰囲気をなるべく合わせていただけると幸いです。(「裏面画像.jpg」)
また、以前に表面のデザインも作成しておりますので、こちらも参考にしてください。(「表面画像.jpg」)

特に、
・往診料無料
・ワクチン料金
・フィラリア症予防薬料金
・自宅で手軽に予防ができる
上記の内容をより訴求できるデザインにしたいと思っております。

動物病院ですので、優しく、特に女性受けが良さそうなイメージで作成をお願いいたします。

使用する色は、主に「緑、オレンジ」をメインに考えておりますが、色の具合は自由に調節いただいて結構です。
作りたいチラシのイメージは、「参考画像.jpg」の通りですが、デザインは自由に調節していただいて結構です。
また、こちらで用意させていただく素材以外で、デザインに沿った文言・イラスト・アイコン・写真などがありましたら、自由に取り入れていただければと思います。
記載項目
・チラシに使用する文章はこちらで用意いたします。

「参考画像.jpg」の①~⑩にはPDFファイル(チラシ記載内容.pdf)に記載されている文章を使用してください。

・院長の画像については、画像1、画像2のいずれかをお使いください。
※psd形式以外のデータをご希望の際はお申し付けください。

・ロゴについては画像3をお使いください。
サイズ
A4
ページ数
片面
希望イメージ
• +5 0 +5
• シンプル
複雑
• 単色
カラフル
• 暗い
明るい
• 日常
高級
• 遊び心
厳粛
• 未来的
伝統的
• 女性的
男性的
希望する色
納品ファイル
• 高解像度JPG (.jpg)
• イラストレーター形式 (.ai)
補足説明
依頼公開後の追記内容
■ 選んだ理由

全体的なイメージと、特に家のデザインが気に入りました。

■ 提案者全員のお礼・コメント

この度はご提案くださり誠にありがとうございました。
どれも良いものばかりで、選択に非常に迷いました。

また機会がございましたら、その時はどうぞよろしくお願いいたします。

```html
<!DOCTYPE html>
<html lang="ja">
<head>
<meta charset="utf-8">
<title>ひなた動物病院 往診ワクチンのご案内</title>
<link href="https://fonts.googleapis.com/css2?family=M+PLUS+Rounded+1c:wght@500;800;900&family=Noto+Sans+JP:wght@400;500;700&display=swap" rel="stylesheet">
<style>
:root{
  --green:#8cc63f;
  --green-dark:#5f9e2a;
  --green-pale:#eef6e0;
  --orange:#f39a2b;
  --orange-pale:#fdf0dc;
  --red:#e8473f;
  --pink:#f27a8a;
  --ink:#3a3a3a;
  --line:#c9d9b0;
  --paper:#ffffff;
}
*{box-sizing:border-box;margin:0;padding:0}
html,body{width:851px;height:1200px;overflow:hidden;background:var(--paper)}
body{font-family:"Noto Sans JP",sans-serif;color:var(--ink)}
.flyer{position:relative;width:851px;height:1200px;overflow:hidden;background:var(--paper)}
.abs{position:absolute}

.hero-photo{left:0;top:0;width:440px;height:335px;background:linear-gradient(160deg,#cfe6f2 0%,#e9d6b4 55%,#b98a55 100%);border-bottom-right-radius:30px}
.tag{border-radius:50%;display:flex;align-items:center;justify-content:center;text-align:center;color:#fff;font-family:"M PLUS Rounded 1c",sans-serif;font-weight:800;line-height:1.25}
.tag-vaccine{left:470px;top:12px;width:96px;height:96px;background:var(--green);font-size:19px}
.tag-filaria{left:572px;top:6px;width:108px;height:108px;background:var(--pink);font-size:18px}
.syringe-art{left:700px;top:0;width:140px;height:110px;background:linear-gradient(135deg,#e6f2fb,#c7dff0);border-radius:0 0 0 60px}

.headline{right:22px;top:118px;text-align:right;font-family:"M PLUS Rounded 1c",sans-serif;font-weight:900;color:var(--red);font-size:76px;line-height:1.02;letter-spacing:-2px}
.free-badge{left:300px;top:290px;width:140px;height:150px;border:5px solid var(--red);background:#fff;transform:rotate(-8deg);display:flex;flex-direction:column;align-items:center;justify-content:center;color:var(--red);font-family:"M PLUS Rounded 1c",sans-serif;font-weight:900;line-height:1.05}
.free-badge .s{font-size:34px}
.free-badge .l{font-size:46px}
.visit{left:452px;top:366px;font-family:"M PLUS Rounded 1c",sans-serif;font-weight:800;font-size:34px;color:var(--ink)}
.contact-lead{left:452px;top:418px;font-family:"M PLUS Rounded 1c",sans-serif;font-weight:800;font-size:28px;color:var(--red)}

.price{top:478px;height:248px;border:2px solid var(--green);background:#fff}
.price-vaccine{left:32px;width:396px}
.price-filaria{left:440px;width:380px}
.price h2{background:var(--green);color:#fff;font-size:17px;text-align:center;height:30px;line-height:30px;font-weight:700}
.grid{display:flex;height:214px}
.side{width:32px;background:var(--green-pale);color:var(--green-dark);font-weight:700;font-size:17px;writing-mode:vertical-rl;display:flex;align-items:center;justify-content:center;border-right:1px solid var(--line)}
.rows{flex:1;display:flex;flex-direction:column}
.rows div{flex:1;display:flex;justify-content:space-between;align-items:center;padding:0 7px;font-size:12.5px;border-bottom:1px solid var(--line)}
.rows div:last-child{border-bottom:none}
.rows b{color:var(--red);font-weight:700}
.ftable{width:100%;border-collapse:collapse;font-size:13px;text-align:center}
.ftable th{background:var(--green-pale);color:var(--green-dark);height:30px;font-weight:700;border-bottom:1px solid var(--line)}
.ftable td{height:30.6px;border-bottom:1px solid var(--line);border-left:1px solid var(--line)}
.ftable td:first-child{border-left:none}
.ftable td.p{color:var(--red);font-weight:700}

.schedule{left:32px;top:736px;width:788px;height:172px;display:flex;border:2px solid var(--orange)}
.sched-title{width:38px;background:var(--orange);color:#fff;writing-mode:vertical-rl;font-weight:700;font-size:16px;display:flex;align-items:center;justify-content:center;letter-spacing:2px}
.sched-rows{flex:1;display:flex;flex-direction:column}
.sched-rows div{flex:1;display:flex;align-items:center;border-bottom:1px solid #f3cfa0;font-size:13px}
.sched-rows div:last-child{border-bottom:none}
.sched-rows span{width:72px;height:100%;display:flex;align-items:center;justify-content:center;background:var(--orange-pale);color:#c96d0a;font-weight:700;margin-right:10px}

.area{left:32px;top:918px;width:580px;height:168px;display:flex;border:2px solid var(--green)}
.area-title{width:38px;background:var(--green);color:#fff;writing-mode:vertical-rl;font-weight:700;font-size:16px;display:flex;align-items:center;justify-content:center;letter-spacing:2px}
.area-rows{flex:1;display:flex;flex-direction:column}
.area-rows div{flex:1;display:flex;align-items:center;border-bottom:1px solid var(--line);font-size:11.5px;line-height:1.35}
.area-rows div:last-child{border-bottom:none}
.area-rows span{width:72px;flex:none;height:100%;display:flex;align-items:center;justify-content:center;background:var(--green-pale);color:var(--green-dark);font-weight:700;font-size:13px;margin-right:8px}
.director{left:626px;top:918px;width:194px;height:168px;background:linear-gradient(180deg,#d9e7ef,#a9bfcc);border-radius:6px}
.director-name{left:626px;top:1062px;width:194px;text-align:center;font-size:13px;font-weight:700;background:rgba(255,255,255,.85);padding:3px 0}

.note{left:32px;top:1094px;width:788px;text-align:center;font-size:12px;color:#666}
.footer{left:0;top:1120px;width:851px;height:80px;background:var(--green-pale);border-top:4px solid var(--green);display:flex;align-items:center;padding:0 32px;gap:16px}
.brand{display:flex;align-items:center;gap:10px}
.brand i{width:30px;height:30px;border-radius:50%;background:var(--orange)}
.brand strong{font-family:"M PLUS Rounded 1c",sans-serif;font-weight:800;font-size:28px;color:var(--green-dark)}
.address{font-size:11px;color:#555;line-height:1.5}
.tel{margin-left:auto;display:flex;align-items:center;gap:6px;color:var(--red);font-family:"M PLUS Rounded 1c",sans-serif;font-weight:900;font-size:34px}
.tel small{font-size:14px;color:var(--ink);font-weight:800}
</style>
</head>
<body>
<main class="flyer">
  <div class="abs hero-photo" role="img" aria-label="獣医師が犬を抱き、猫と子犬が寄り添う家のイラストと写真"></div>
  <div class="abs tag tag-vaccine">自宅で<br>ワクチン</div>
  <div class="abs tag tag-filaria">自宅で<br>フィラリア<br>予防</div>
  <div class="abs syringe-art" role="img" aria-label="注射器のイラスト"></div>

  <h1 class="abs headline">ワクチンは<br>おウチでが<br>新しい!</h1>
  <div class="abs free-badge"><span class="s">往診料</span><span class="l">無料</span></div>
  <p class="abs visit">でお伺いします!</p>
  <p class="abs contact-lead">お気軽にご連絡ください。</p>

  <section class="abs price price-vaccine">
    <h2>ワクチン料金表</h2>
    <div class="grid">
      <div class="side">犬用</div>
      <div class="rows">
        <div>狂犬病ワクチン<b>2,500円</b></div>
        <div>5種混合ワクチン<b>5,000円</b></div>
        <div>6種混合ワクチン<b>5,500円</b></div>
        <div>8種混合ワクチン<b>6,000円</b></div>
      </div>
      <div class="side" style="border-left:1px solid var(--line)">猫用</div>
      <div class="rows">
        <div>3種混合ワクチン<b>4,000円</b></div>
        <div>5種混合ワクチン<b>5,000円</b></div>
        <div>白血病ワクチン<b>4,500円</b></div>
        <div>&nbsp;</div>
      </div>
    </div>
  </section>

  <section class="abs price price-filaria">
    <h2>フィラリア予防薬料金表</h2>
    <table class="ftable">
      <tr><th>体重</th><th>1回分</th><th>7回分セット</th></tr>
      <tr><td>5kg未満</td><td class="p">600円</td><td class="p">4,200円</td></tr>
      <tr><td>5kg以上</td><td class="p">600円</td><td class="p">4,200円</td></tr>
      <tr><td>10kg以上</td><td class="p">600円</td><td class="p">4,200円</td></tr>
      <tr><td>15kg以上</td><td class="p">600円</td><td class="p">4,200円</td></tr>
      <tr><td>20kg以上</td><td class="p">600円</td><td class="p">4,200円</td></tr>
      <tr><td>30kg以上</td><td class="p">600円</td><td class="p">4,200円</td></tr>
    </table>
  </section>

  <section class="abs schedule">
    <div class="sched-title">往診スケジュール</div>
    <div class="sched-rows">
      <div><span>栃木県</span>4/1(水)〜4/3(金)、4/24(金)〜4/28(火)、5/11(月)〜5/14(木)、5/22(金)〜5/24(日)</div>
      <div><span>群馬県</span>4/5(日)〜4/8(水)、4/20(月)〜4/23(木)、5/15(金)〜5/21(木)</div>
      <div><span>埼玉県</span>4/9(木)〜4/12(日)、4/17(金)〜4/19(日)、5/7(木)〜5/10(日)</div>
      <div><span>東京都</span>4/10(金)〜4/12(日)、4/27(月)〜4/30(木)、5/4(月)〜5/7(木)</div>
      <div><span>神奈川県</span>4/13(月)〜4/16(木)、5/1(金)〜5/3(日)</div>
    </div>
  </section>

  <section class="abs area">
    <div class="area-title">往診エリア</div>
    <div class="area-rows">
      <div><span>栃木県</span>宇都宮市、足利市、佐野市、小山市、栃木市、鹿沼市、真岡市、下野市、壬生町ほか</div>
      <div><span>群馬県</span>前橋市、高崎市、桐生市、伊勢崎市、太田市、館林市、みどり市ほか</div>
      <div><span>埼玉県</span>全域</div>
      <div><span>東京都</span>全域</div>
      <div><span>神奈川県</span>横浜市、川崎市、相模原市、藤沢市、大和市、厚木市ほか</div>
    </div>
  </section>
  <div class="abs director" role="img" aria-label="院長の写真"></div>
  <p class="abs director-name">院長　森田 健</p>

  <p class="abs note">上記以外の日程・地域もご相談ください。お気軽にお問い合わせください。</p>

  <footer class="abs footer">
    <div class="brand"><i></i><strong>ひなた動物病院</strong></div>
    <p class="address">〒376-0000 栃木県みどり市ひなた町1-2-3<br>TEL 0277-00-1122　hinata-ah.example.jp</p>
    <div class="tel">
      <svg width="30" height="30" viewBox="0 0 24 24" aria-hidden="true"><path fill="#e8473f" d="M6.6 10.8a15.1 15.1 0 0 0 6.6 6.6l2.2-2.2a1 1 0 0 1 1-.25 11.4 11.4 0 0 0 3.6.57 1 1 0 0 1 1 1V20a1 1 0 0 1-1 1A17 17 0 0 1 3 4a1 1 0 0 1 1-1h3.5a1 1 0 0 1 1 1c0 1.25.2 2.45.57 3.57a1 1 0 0 1-.25 1z"/></svg>
      <small>Tel</small>080-2471-3586
    </div>
  </footer>
</main>
</body>
</html>
```